User-interface and web design for new forum-style communication platform

We developed a new forum-style communication platform specially targetting stock investors to share and discuss information on companies listed on the stock exchange.

You have complete freedom for designing the user-interface and web design. Designs should include all features listed below.

Please read the attached document for full specifications. Also attached is a mockup of the layout, but this is only directional. A mockup for the user-profile is also attached, but does not need to be designed.

This project focusses on the homepage and thread view.

The winner(s) will be asked to design the complete project. (create thread box, user profile, registering, settings...)

We are looking for a well thought out, smart design that incorporates the specifications in the attached document. Please do not hesitate to contact us if anything is not clear.

Target Market(s)

Stock investors from 25 to 60 years old (the people that are currently on investor forums)

Industry/Entity Type

Communication

Font styles to use
Sans Serif

Colors

Designer to choose colors to be used in the design.

Requirements
Must have
• Full homepage design & Thread view specified in the attached document.
Nice to have
• Create thread view
- Field for adding tags
- field for subject of the thread
- text box with basic text editing
- method for sharing media
Should not have
• Logo design.

```html
<!DOCTYPE html>
<html lang="en">
<head>
<meta charset="utf-8">
<title>Tradora – Conversations</title>
<link href="https://fonts.googleapis.com/css2?family=Montserrat:wght@400;500;600;700&display=swap" rel="stylesheet">
<style>
:root{
  --blue:#0b6fb8;
  --blue-dark:#0a4f86;
  --navy:#0d3f66;
  --ink:#1c1c1c;
  --muted:#555;
  --page:#f5f5f5;
  --band:#ebebeb;
  --card:#ffffff;
  --line:#e3e3e3;
  --red:#e0262b;
  --black:#111;
}
*{box-sizing:border-box;margin:0;padding:0}
html,body{width:928px;height:1200px;overflow:hidden}
body{font-family:"Montserrat",Arial,sans-serif;background:var(--page);color:var(--ink);position:relative;font-size:10px}
a{color:var(--blue);text-decoration:none}

.site-header{position:absolute;left:0;top:0;width:928px;height:69px;background:var(--band)}
.brand{position:absolute;left:126px;top:22px;display:flex;align-items:center;gap:6px;font-weight:700;font-size:22px;color:var(--blue)}
.brand-dot{width:12px;height:12px;border-radius:50%;background:var(--blue)}
.tag-search{position:absolute;left:297px;top:22px;width:359px;height:31px;background:#fff;border:1px solid #cfcfcf;border-radius:16px 0 0 16px;display:flex;align-items:center;padding-left:8px}
.tag-search span{color:#aaa;font-size:10px;margin-left:4px;flex:1}
.btn{display:inline-flex;align-items:center;justify-content:center;color:#fff;font-size:10px;height:19px;border:0}
.btn-blue{background:var(--blue)}
.btn-navy{background:var(--navy)}
.btn-black{background:var(--black)}
.tag-search .btn{height:20px;margin-right:4px}
.notify-tip{position:absolute;left:677px;top:4px;width:60px;height:17px;background:var(--blue);color:#fff;font-size:6px;display:flex;align-items:center;justify-content:center;border-radius:2px}
.notify-tip::after{content:"";position:absolute;left:22px;bottom:-4px;border:4px solid transparent;border-top-color:var(--blue);border-bottom:0}
.notify-badge{position:absolute;left:697px;top:26px;width:19px;height:19px;border-radius:50%;background:var(--red);color:#fff;font-size:11px;display:flex;align-items:center;justify-content:center}
.user-menu{position:absolute;left:758px;top:26px;width:47px;height:21px}

.sidebar{position:absolute;left:126px;top:110px;width:158px}
.side-box{background:var(--page);box-shadow:0 1px 3px rgba(0,0,0,.12);padding:8px 8px 8px;margin-bottom:16px}
.side-head{display:flex;justify-content:space-between;align-items:baseline;padding:2px 2px 8px}
.side-head h3{font-size:10px;font-weight:600;color:var(--blue)}
.side-head a,.show-all{font-size:8px;color:var(--muted);text-decoration:underline}
.side-search{background:#fff;border-radius:10px;height:20px;display:flex;align-items:center;padding-left:6px;color:#bbb;font-size:7px;gap:4px}
.side-list{background:#fff;list-style:none;padding:9px 10px 4px}
.side-list li{display:flex;align-items:center;gap:7px;font-size:8px;height:15px;color:var(--muted)}
.side-list li.group{font-weight:600;color:var(--ink);height:21px}
.side-list li.sub{padding-left:2px}
.ic{width:9px;height:9px;border-radius:50%;background:#9a9a9a;color:#fff;font-size:8px;line-height:9px;text-align:center;font-weight:700}
.chev{color:#888;width:9px;text-align:center}
.side-actions{display:flex;gap:4px;margin-top:8px}
.side-actions .btn{width:52px;height:20px}
.show-all{display:block;margin:12px 2px 0}

.main{position:absolute;left:298px;top:110px;width:507px}
.crumbs{font-size:10px;font-weight:600;color:var(--blue);height:18px}
.crumbs span{color:var(--ink);font-weight:400}
.tabs-row{display:flex;justify-content:space-between;margin-top:10px}
.tabs{display:flex}
.tabs .btn{height:21px;width:87px}
.tabs .btn-black{width:82px}
.tabs-row .btn-create{height:21px;width:82px}

.post{background:var(--card);box-shadow:0 1px 3px rgba(0,0,0,.1);margin-top:33px;height:214px}
.post+.reply{margin-top:12px}
.post-body{display:flex;padding:14px 10px 0;height:169px;border-bottom:1px solid var(--line)}
.post-side{width:108px}
.post-thumb{width:90px;height:82px;background:linear-gradient(135deg,#0b2a63,#1b63c4 55%,#0c3a2a)}
.post-side a{display:flex;align-items:center;gap:6px;font-size:8px;margin-top:7px}
.post-side a + a{margin-top:5px}
.post-text h2{font-size:9.5px;font-weight:700;color:var(--blue);margin-bottom:5px}
.post-meta{font-size:9.5px;margin-bottom:3px}
.post-text p{font-size:9.5px;line-height:17px;color:#333;width:375px}
.post-text .btn{width:82px;height:20px;font-weight:700;margin-top:5px}
.post-foot{display:flex;align-items:center;justify-content:space-between;height:45px;padding:0 9px 0 10px}
.stats{display:flex;align-items:center;gap:6px;font-size:10px}
.stats svg{display:block}
.actions{display:flex;gap:3px}
.actions .btn{width:57px;height:20px;font-size:10px}

.reply{display:flex;justify-content:space-between;height:64px;margin-top:12px}
.reply-brand{width:69px;background:#efefef;box-shadow:0 1px 3px rgba(0,0,0,.12);display:flex;align-items:center;justify-content:center;color:var(--blue);font-weight:700;font-size:13px}
.reply-field{width:425px;background:#fff;box-shadow:inset 0 0 6px rgba(0,0,0,.12);padding:12px 15px;font-size:8px;color:var(--muted)}

.site-footer{position:absolute;left:0;top:1134px;width:928px;height:66px;background:var(--band)}
.site-footer p{position:absolute;left:0;right:0;top:28px;text-align:center;font-size:10px;color:#333}
.social{position:absolute;left:770px;top:28px;display:flex;gap:8px}
.social .round{width:14px;height:14px;border-radius:50%;background:var(--blue)}
.social .square{width:14px;height:14px;background:var(--blue-dark)}
</style>
</head>
<body>
<header class="site-header">
  <div class="brand"><span class="brand-dot"></span>Tradora</div>
  <div class="tag-search">
    <svg width="13" height="13" viewBox="0 0 14 14"><circle cx="5.5" cy="5.5" r="4.2" fill="none" stroke="#555" stroke-width="1.6"/><path d="M8.5 8.5l4.5 4.5" stroke="#555" stroke-width="2"/></svg>
    <span>Enter Name for tagfilter</span>
    <button class="btn btn-blue" style="width:51px">Save</button>
    <button class="btn btn-black" style="width:51px">Clear</button>
  </div>
  <div class="notify-tip">1 New Followers</div>
  <div class="notify-badge">3</div>
  <button class="btn btn-blue user-menu">User ▾</button>
</header>

<aside class="sidebar">
  <section class="side-box">
    <div class="side-head"><h3>Users</h3></div>
    <div class="side-search">
      <svg width="10" height="10" viewBox="0 0 14 14"><circle cx="5.5" cy="5.5" r="4.2" fill="none" stroke="#444" stroke-width="1.6"/><path d="M8.5 8.5l4.5 4.5" stroke="#444" stroke-width="2"/></svg>Search
    </div>
  </section>

  <section class="side-box">
    <div class="side-head"><h3>Saved Filters</h3><a href="#">Show All</a></div>
    <ul class="side-list">
      <li class="group"><span class="ic">–</span>Item Name 1</li>
      <li class="sub"><span class="chev">›</span>Item Name 1</li>
      <li class="sub"><span class="chev">›</span>Item Name 2</li>
      <li class="sub"><span class="chev">›</span>Item Name 3</li>
      <li class="sub"><span class="chev">›</span>Item Name 4</li>
      <li class="group"><span class="ic">+</span>Item Name 2</li>
      <li class="group"><span class="ic">+</span>Item Name 3</li>
      <li class="group"><span class="ic">+</span>Item Name 4</li>
    </ul>
    <div class="side-actions"><button class="btn btn-blue">Rename</button><button class="btn btn-blue">Delete</button></div>
  </section>

  <section class="side-box">
    <div class="side-head"><h3>Popular Tags</h3></div>
    <ul class="side-list">
      <li class="group"><span class="ic">–</span>Item Name 1</li>
      <li class="sub"><span class="chev">›</span>Item Name 1</li>
      <li class="sub"><span class="chev">›</span>Item Name 2</li>
      <li class="sub"><span class="chev">›</span>Item Name 3</li>
      <li class="sub"><span class="chev">›</span>Item Name 4</li>
      <li class="group"><span class="ic">+</span>Item Name 2</li>
      <li class="group"><span class="ic">+</span>Item Name 3</li>
      <li class="group"><span class="ic">+</span>Item Name 4</li>
    </ul>
    <a class="show-all" href="#">Show All</a>
  </section>

  <section class="side-box">
    <div class="side-head"><h3>Popular Contributers</h3></div>
    <ul class="side-list">
      <li class="group"><span class="ic">–</span>Item Name 1</li>
      <li class="sub"><span class="chev">›</span>Item Name 1</li>
      <li class="sub"><span class="chev">›</span>Item Name 2</li>
      <li class="sub"><span class="chev">›</span>Item Name 3</li>
      <li class="sub"><span class="chev">›</span>Item Name 4</li>
      <li class="group"><span class="ic">+</span>Item Name 2</li>
      <li class="group"><span class="ic">+</span>Item Name 3</li>
      <li class="group"><span class="ic">+</span>Item Name 4</li>
    </ul>
    <a class="show-all" href="#">Show All</a>
  </section>
</aside>

<main class="main">
  <div class="crumbs">Home &gt; Conversations &gt; Public &gt; <span># northwind # larkspur</span></div>
  <div class="tabs-row">
    <div class="tabs">
      <button class="btn btn-blue">Public</button>
      <button class="btn btn-navy">Following</button>
      <button class="btn btn-black">Contacts</button>
    </div>
    <button class="btn btn-blue btn-create">Create Thread</button>
  </div>

  <article class="post" style="margin-top:33px">
    <div class="post-body">
      <div class="post-side">
        <div class="post-thumb" role="img" aria-label="Stock market chart on a glowing screen"></div>
        <a href="#"><svg width="9" height="9" viewBox="0 0 10 10"><circle cx="5" cy="3" r="2.4" fill="#555"/><path d="M0.5 10c0-3 2-4.5 4.5-4.5S9.5 7 9.5 10z" fill="#555"/></svg>View Profile</a>
        <a href="#"><svg width="10" height="8" viewBox="0 0 10 8"><rect width="10" height="8" fill="#555"/><path d="M0 0l5 4.5L10 0" fill="none" stroke="#fff" stroke-width="1"/></svg>View All Posts</a>
      </div>
      <div class="post-text">
        <h2>Neque porro quisquam est qui dolorem ipsum quia dolor sit</h2>
        <div class="post-meta">Posed by Marten Vos on 31-02-2014 at 15:23</div>
        <p>Lorem Ipsum is simply dummy text of the printing and typesetting industry. Lorem Ipsum has been the industry's standard dummy text ever since the 1500s, when an unknown printer took a galley of type and scrambled it to make a type specimen book. It has survived not only five centuries, but also the leap into electronic typesetting...</p>
        <button class="btn btn-blue">Read More</button>
      </div>
    </div>
    <div class="post-foot">
      <div class="stats">
        <svg width="14" height="13" viewBox="0 0 14 13"><path d="M1 12C1 6 4 4 9 4V1l5 4.5L9 10V7C5 7 3 8 1 12z" fill="#333"/></svg>12 Replies
        <svg width="16" height="10" viewBox="0 0 16 10" style="margin-left:4px"><ellipse cx="8" cy="5" rx="8" ry="5" fill="#333"/><circle cx="8" cy="5" r="2.3" fill="#fff"/></svg>250 Views
      </div>
      <div class="actions"><button class="btn btn-blue">Reply</button><button class="btn btn-navy">Share</button><button class="btn btn-black">Favourite</button></div>
    </div>
  </article>
  <div class="reply"><div class="reply-brand">Tradora</div><div class="reply-field">Typr Your reply</div></div>

  <article class="post" style="margin-top:18px">
    <div class="post-body">
      <div class="post-side">
        <div class="post-thumb" role="img" aria-label="Tablet showing a green market chart" style="background:linear-gradient(135deg,#c9d3da,#3a4c5c 45%,#1e6a4a)"></div>
        <a href="#"><svg width="9" height="9" viewBox="0 0 10 10"><circle cx="5" cy="3" r="2.4" fill="#555"/><path d="M0.5 10c0-3 2-4.5 4.5-4.5S9.5 7 9.5 10z" fill="#555"/></svg>View Profile</a>
        <a href="#"><svg width="10" height="8" viewBox="0 0 10 8"><rect width="10" height="8" fill="#555"/><path d="M0 0l5 4.5L10 0" fill="none" stroke="#fff" stroke-width="1"/></svg>View All Posts</a>
      </div>
      <div class="post-text">
        <h2>Neque porro quisquam est qui dolorem ipsum quia dolor sit</h2>
        <div class="post-meta">Posed by Marten Vos on 31-02-2014 at 15:23</div>
        <p>Lorem Ipsum is simply dummy text of the printing and typesetting industry. Lorem Ipsum has been the industry's standard dummy text ever since the 1500s, when an unknown printer took a galley of type and scrambled it to make a type specimen book. It has survived not only five centuries, but also the leap into electronic typesetting...</p>
        <button class="btn btn-blue">Read More</button>
      </div>
    </div>
    <div class="post-foot">
      <div class="stats">
        <svg width="14" height="13" viewBox="0 0 14 13"><path d="M1 12C1 6 4 4 9 4V1l5 4.5L9 10V7C5 7 3 8 1 12z" fill="#333"/></svg>12 Replies
        <svg width="16" height="10" viewBox="0 0 16 10" style="margin-left:4px"><ellipse cx="8" cy="5" rx="8" ry="5" fill="#333"/><circle cx="8" cy="5" r="2.3" fill="#fff"/></svg>250 Views
      </div>
      <div class="actions"><button class="btn btn-blue">Reply</button><button class="btn btn-navy">Share</button><button class="btn btn-black">Favourite</button></div>
    </div>
  </article>
  <div class="reply"><div class="reply-brand">Tradora</div><div class="reply-field">Typr Your reply</div></div>

  <article class="post" style="margin-top:10px">
    <div class="post-body">
      <div class="post-side">
        <div class="post-thumb" role="img" aria-label="Blue market chart with a pen pointing at the line" style="background:linear-gradient(135deg,#0a1f4a,#1d55b0 55%,#0b1a33)"></div>
        <a href="#"><svg width="9" height="9" viewBox="0 0 10 10"><circle cx="5" cy="3" r="2.4" fill="#555"/><path d="M0.5 10c0-3 2-4.5 4.5-4.5S9.5 7 9.5 10z" fill="#555"/></svg>View Profile</a>
        <a href="#"><svg width="10" height="8" viewBox="0 0 10 8"><rect width="10" height="8" fill="#555"/><path d="M0 0l5 4.5L10 0" fill="none" stroke="#fff" stroke-width="1"/></svg>View All Posts</a>
      </div>
      <div class="post-text">
        <h2>Neque porro quisquam est qui dolorem ipsum quia dolor sit</h2>
        <div class="post-meta">Posed by Marten Vos on 31-02-2014 at 15:23</div>
        <p>Lorem Ipsum is simply dummy text of the printing and typesetting industry. Lorem Ipsum has been the industry's standard dummy text ever since the 1500s, when an unknown printer took a galley of type and scrambled it to make a type specimen book. It has survived not only five centuries, but also the leap into electronic typesetting...</p>
        <button class="btn btn-blue">Read More</button>
      </div>
    </div>
    <div class="post-foot">
      <div class="stats">
        <svg width="14" height="13" viewBox="0 0 14 13"><path d="M1 12C1 6 4 4 9 4V1l5 4.5L9 10V7C5 7 3 8 1 12z" fill="#333"/></svg>12 Replies
        <svg width="16" height="10" viewBox="0 0 16 10" style="margin-left:4px"><ellipse cx="8" cy="5" rx="8" ry="5" fill="#333"/><circle cx="8" cy="5" r="2.3" fill="#fff"/></svg>250 Views
      </div>
      <div class="actions"><button class="btn btn-blue">Reply</button><button class="btn btn-navy">Share</button><button class="btn btn-black">Favourite</button></div>
    </div>
  </article>
  <div class="reply"><div class="reply-brand">Tradora</div><div class="reply-field">Typr Your reply</div></div>
</main>

<footer class="site-footer">
  <p>© 2014 Company Name ,All Rights reserved</p>
  <div class="social"><span class="round"></span><span class="square"></span></div>
</footer>
</body>
</html>
```